this is a new company aimed at the automotive glass industry
what we do is repair cracked windscreens its based in western austraila
I like the old dragracing signwritting logos
I want it to stand out thats why ive gone with the name and title
I dont have a logo but if you can think of one that would be great
but not essential
on the back of the business card i would like Quicker Cheaper Better

Reason: More time needed to decide some great designs Have come through on the eleventh

Target Market(s)

automotive (car yards ,car auctions , trucking companys ect )

Industry/Entity Type

Automotive

Contact Information for Business Card

Pane Stoppers ,
Glass Crack repair specialists ,
Dorian Pelletier ,0437 612 084 ,dpelletier@panestopperswa.com.au

```html
<!DOCTYPE html>
<html lang="en">
<head>
<meta charset="utf-8">
<title>Pane Stoppers – Business Card</title>
<link rel="stylesheet" href="https://fonts.googleapis.com/css2?family=Kaushan+Script&family=Open+Sans:wght@400;600;700&display=swap">
<style>
  :root {
    --page-bg: #3a3a3a;
    --card-dark: #121416;
    --card-dark-edge: #23272a;
    --card-light: #f1f1f1;
    --card-light-edge: #dcdcdc;
    --text-light: #ffffff;
    --text-dark: #1a1a1a;
    --icon-grey: #3c4447;
    --glass-teal: #7fa7a6;
    --glass-deep: #2e4a4f;
    --silver-hi: #f4f4f4;
    --silver-lo: #5a5e61;
  }
  * { box-sizing: border-box; margin: 0; padding: 0; }
  html, body { width: 1200px; height: 750px; overflow: hidden; }
  body {
    background: var(--page-bg);
    font-family: "Open Sans", Arial, sans-serif;
    position: relative;
  }
  .card {
    position: absolute;
    top: 225px;
    width: 520px;
    height: 300px;
    border-radius: 18px;
    overflow: hidden;
  }
  .card--front { left: 60px; background: var(--card-light); }
  .card--back {
    left: 620px;
    background: radial-gradient(ellipse at 60% 40%, var(--card-dark-edge), var(--card-dark) 75%);
  }

  /* Signwriter display lettering */
  .brand-name,
  .back-name {
    position: absolute;
    font-family: "Kaushan Script", "Brush Script MT", cursive;
    font-weight: 400;
    line-height: 1;
    color: var(--text-light);
    white-space: nowrap;
  }

  /* Front */
  .front-header {
    position: absolute; left: 0; top: 0; width: 520px; height: 180px;
    background: linear-gradient(180deg, var(--card-dark) 0%, var(--card-dark-edge) 100%);
  }
  .silver-band {
    position: absolute; left: 0; top: 180px; width: 520px; height: 13px;
    background: linear-gradient(90deg, var(--silver-lo) 0%, var(--silver-hi) 30%, var(--silver-lo) 55%, var(--silver-hi) 80%, var(--silver-lo) 100%);
    border-bottom: 3px solid var(--card-dark);
  }
  .front-footer {
    position: absolute; left: 0; top: 196px; width: 520px; height: 104px;
    background: linear-gradient(160deg, var(--card-light) 0%, var(--card-light-edge) 50%, var(--card-light) 100%);
  }
  .brand-name { left: 30px; top: 68px; font-size: 40px; }
  .brand-tagline {
    position: absolute; left: 30px; top: 120px;
    font-size: 17px; color: var(--text-light); white-space: nowrap;
  }
  .photo-cluster { position: absolute; left: 0; top: 0; }
  .contact-person { position: absolute; left: 26px; top: 230px; color: var(--text-dark); }
  .contact-person .person-name { font-size: 16px; line-height: 1.15; }
  .contact-person .person-role { font-size: 12.5px; line-height: 1.2; }
  .contact-lines { position: absolute; left: 236px; top: 229px; color: var(--text-dark); font-size: 14.5px; }
  .contact-line { display: flex; align-items: center; gap: 10px; height: 22px; white-space: nowrap; }
  .contact-line svg { flex: none; }

  /* Back */
  .glass-burst { position: absolute; left: 0; top: 0; }
  .back-name { left: 128px; top: 110px; font-size: 44px; }
  .back-tagline {
    position: absolute; left: 130px; top: 166px;
    font-size: 17px; color: var(--text-light); white-space: nowrap;
  }
  .back-slogan {
    position: absolute; left: 130px; top: 204px;
    font-size: 14px; font-weight: 600; letter-spacing: 3px;
    text-transform: uppercase; color: var(--glass-teal); white-space: nowrap;
  }
</style>
</head>
<body>

<section class="card card--front">
  <div class="front-header"></div>
  <div class="silver-band"></div>
  <div class="front-footer"></div>

  <svg class="photo-cluster" width="520" height="300" viewBox="0 0 520 300" role="img" aria-label="Photos of a technician repairing a cracked car windscreen">
    <defs>
      <linearGradient id="photoTone" x1="0" y1="0" x2="1" y2="1">
        <stop offset="0" stop-color="#9fb4b8"/>
        <stop offset="1" stop-color="#3f5a60"/>
      </linearGradient>
    </defs>
    <polygon points="413,22 470,22 496,68 470,115 413,115 388,68" fill="url(#photoTone)"/>
    <polygon points="327,65 386,65 412,109 386,153 327,153 302,109" fill="url(#photoTone)"/>
    <polygon points="412,112 470,112 496,156 470,199 412,199 386,156" fill="url(#photoTone)"/>
  </svg>

  <div class="brand-name">Pane Stoppers</div>
  <div class="brand-tagline">Glass Crack repair specialists</div>

  <div class="contact-person">
    <div class="person-name">Dorian Pelletier</div>
    <div class="person-role">Glass Crack repair specialists</div>
  </div>

  <div class="contact-lines">
    <div class="contact-line">
      <svg width="15" height="12" viewBox="0 0 15 12" aria-hidden="true">
        <path d="M1 4 Q7.5 -1 14 4 L12 6 L10 4.5 L5 4.5 L3 6 Z" fill="var(--icon-grey)"/>
        <rect x="3" y="6" width="9" height="6" rx="1" fill="var(--icon-grey)"/>
      </svg>
      <span>0437 612 084</span>
    </div>
    <div class="contact-line">
      <svg width="15" height="11" viewBox="0 0 15 11" aria-hidden="true">
        <rect x="0.5" y="0.5" width="14" height="10" fill="var(--icon-grey)"/>
        <path d="M0.5 0.5 L7.5 6 L14.5 0.5" stroke="var(--card-light)" stroke-width="1.2" fill="none"/>
      </svg>
      <span>dpelletier@panestopperswa.com.au</span>
    </div>
  </div>
</section>

<section class="card card--back">
  <svg class="glass-burst" width="520" height="300" viewBox="0 0 520 300" role="img" aria-label="Illustration of a shattered glass crack radiating outward">
    <defs>
      <radialGradient id="crackTone" cx="0.5" cy="0.5" r="0.5">
        <stop offset="0" stop-color="var(--glass-teal)" stop-opacity="0.5"/>
        <stop offset="0.6" stop-color="var(--glass-deep)" stop-opacity="0.3"/>
        <stop offset="1" stop-color="var(--glass-deep)" stop-opacity="0"/>
      </radialGradient>
    </defs>
    <circle cx="390" cy="145" r="160" fill="url(#crackTone)"/>
  </svg>

  <div class="back-name">Pane Stoppers</div>
  <div class="back-tagline">Glass Crack repair specialists</div>
  <div class="back-slogan">Quicker · Cheaper · Better</div>
</section>

</body>
</html>
```